Brantley Fuel Retro Website Design

Have a logo. Need a website design to go along with the logo design. Full Design Specs are here: https://files.quormbex.net/doc/8QwLp2ZtR4vNx7sYh3JkM9aDc5Ub6FgTe1WiO0rVn2X/view

Target Market(s)

Independent Gas Station Owners

Number of Pages Required

1 page

Font styles to use
Sans Serif

Colors

Designer to choose colors to be used in the design.

```html
<!DOCTYPE html>
<html lang="en">
<head>
<meta charset="utf-8">
<title>Brantley Fuel</title>
<link href="https://fonts.googleapis.com/css2?family=Oswald:wght@500;600&family=Bitter:wght@400;600&family=Dancing+Script:wght@500&display=swap" rel="stylesheet">
<style>
:root{
  --paper:#efeeec;
  --ink:#231f20;
  --ink-soft:#3a3637;
  --red:#e3262e;
  --grey:#5b5758;
  --line:#c9c7c5;
  --white:#ffffff;
}
*{margin:0;padding:0;box-sizing:border-box}
html,body{width:985px;height:1200px;overflow:hidden}
body{background:var(--paper);font-family:'Bitter',serif;color:var(--grey);position:relative}
.abs{position:absolute}

/* header */
.call{left:228px;top:20px;font-family:'Dancing Script',cursive;font-size:16px;color:var(--ink)}
.call span{color:var(--red)}
.social{display:flex;gap:6px}
.social i{display:block;width:23px;height:23px;border:1px solid var(--red);border-radius:50%}
.social i.on{background:var(--red)}
.social.top{left:616px;top:20px}
.ribbon{left:148px;top:63px}
.nav{left:171px;top:63px;width:643px;height:24px}
.nav a{position:absolute;top:3px;transform:translateX(-50%);font-family:'Oswald',sans-serif;font-size:13px;color:var(--white);text-decoration:none;text-transform:uppercase;letter-spacing:.5px}
.nav a.active{color:var(--red)}
.nav b{position:absolute;top:4px;font-size:10px;color:var(--white);font-family:'Oswald',sans-serif}
.brand-disc{left:449px;top:11px;width:86px;height:86px;border-radius:50%;background:var(--ink-soft);border:3px solid var(--paper);box-shadow:0 0 0 1px var(--line)}
.brand-name{left:449px;top:33px;width:86px;text-align:center;font-family:'Oswald',sans-serif;font-weight:600;font-size:15px;line-height:18px;color:var(--white);text-transform:uppercase;letter-spacing:.5px}

/* hero */
.hero{left:171px;top:122px;width:643px;height:289px;background:linear-gradient(180deg,#c9c4b9 0%,#a9a398 45%,#6d695f 70%,#8f8a80 100%);box-shadow:0 10px 12px -8px rgba(0,0,0,.35)}
.tag{left:171px;height:28px;font-family:'Oswald',sans-serif;text-transform:uppercase;padding-left:23px;line-height:28px;white-space:nowrap}
.tag.hey{top:324px;width:116px;background:var(--red);color:var(--white);font-size:15px;clip-path:polygon(0 0,100% 0,92% 100%,0 100%)}
.tag.welcome{top:353px;width:218px;background:var(--ink);color:var(--red);font-size:15px;clip-path:polygon(0 0,94% 0,100% 50%,94% 100%,0 100%)}
.dots{left:469px;top:429px;display:flex;gap:5px}
.dots i{width:8px;height:8px;border:1px solid var(--ink);border-radius:50%}
.dots i.on{background:radial-gradient(var(--ink) 35%,transparent 40%)}

/* intro */
.divider{left:171px;width:643px;height:6px}
.divider::before,.divider::after{content:"";position:absolute;top:0;width:300px;height:4px;border-top:1px solid var(--line);border-bottom:1px solid var(--line)}
.divider::before{left:0}.divider::after{right:0}
.divider i{position:absolute;left:312px;top:-6px;width:18px;height:18px;border-radius:50%;background:var(--red)}
.intro{left:171px;top:497px;width:643px;text-align:center;font-family:'Oswald',sans-serif;font-weight:500;font-size:15px;line-height:21px;color:var(--red);text-transform:uppercase;white-space:nowrap;text-shadow:1px 1px 0 var(--ink)}

/* services */
.service{top:591px;width:148px;text-align:center}
.service .photo{width:138px;height:138px;margin:0 auto;border-radius:50%;border:1px solid var(--grey);padding:5px;background-clip:content-box}
.service .label{position:relative;margin-top:-16px;height:27px;border:1px solid var(--grey);border-radius:6px;background:var(--white);font-family:'Oswald',sans-serif;font-size:16px;line-height:25px;color:var(--ink-soft);text-transform:uppercase}
.service p{margin-top:9px;font-size:9px;line-height:13px;padding:0 4px}
.service a{display:inline-block;margin-top:10px;font-size:9px;font-weight:600;color:var(--ink);text-decoration:none;border-bottom:1px solid var(--grey);padding:0 4px}
.service a.hover{color:var(--red);border-color:var(--red)}

/* footer */
.footer-band{left:0;top:905px;width:985px;height:295px;background:var(--ink)}
.cta{left:171px;top:862px;width:643px;height:86px;background:var(--red);border-radius:18px;box-shadow:inset 0 0 0 3px var(--red),inset 0 0 0 4px var(--white)}
.cta-text{left:208px;top:894px;font-family:'Oswald',sans-serif;font-size:14px;color:var(--ink);text-transform:uppercase;white-space:nowrap}
.cta-text span{color:var(--white)}
.cta-btn{left:666px;top:893px;width:93px;height:23px;background:var(--ink);color:var(--white);font-size:9px;font-weight:600;text-align:center;line-height:23px;clip-path:polygon(0 0,88% 0,100% 50%,88% 100%,0 100%,8% 50%)}
.col-title{top:995px;font-family:'Oswald',sans-serif;font-size:13px;color:var(--white);text-transform:uppercase}
.foot{font-size:9px;line-height:17px;color:#b7b3b2}
.foot .hi{color:var(--red);font-weight:600;font-size:11px}
.subscribe{left:666px;top:1023px;width:148px;height:23px;border-radius:12px;background:#3d393a;font-size:8px;color:#a5a1a0;line-height:23px;padding-left:11px}
.subscribe svg{position:absolute;right:10px;top:7px}
.social.bottom{left:666px;top:1058px}
.rule{left:0;top:1150px;width:985px;border-top:1px dashed #3d393a}
.copy{left:171px;top:1168px;font-size:9px;color:#b7b3b2}
.copy span{color:var(--red)}
</style>
</head>
<body>

<div class="abs call"><span>Call Us:</span> (555) 214-7730</div>
<div class="abs social top"><i></i><i class="on"></i><i></i><i></i><i></i></div>

<svg class="abs ribbon" width="695" height="30" viewBox="0 0 695 30" aria-hidden="true">
  <polygon points="0,6 23,6 23,30 0,30 10,18" fill="#3a3637"/>
  <polygon points="695,6 672,6 672,30 695,30 685,18" fill="#3a3637"/>
  <rect x="23" y="0" width="649" height="24" fill="#3a3637"/>
  <line x1="23" y1="3" x2="672" y2="3" stroke="#8a8687" stroke-dasharray="2 2"/>
  <line x1="23" y1="21" x2="672" y2="21" stroke="#8a8687" stroke-dasharray="2 2"/>
</svg>
<nav class="abs nav">
  <a class="active" style="left:40px">Home</a><b style="left:78px">//</b>
  <a style="left:119px">About</a><b style="left:159px">//</b>
  <a style="left:207px">Services</a>
  <a style="left:424px">Blog</a><b style="left:459px">//</b>
  <a style="left:505px">Review</a><b style="left:548px">//</b>
  <a style="left:594px">Contact</a>
</nav>
<div class="abs brand-disc"></div>
<div class="abs brand-name">Brantley<br>Fuel</div>

<div class="abs hero" role="img" aria-label="Sepia photograph of vintage fuel delivery trucks and workers lined up beside an old depot and storage tanks"></div>
<div class="abs tag hey">Hey there!</div>
<div class="abs tag welcome">Welcome to Brantley Fuel</div>
<div class="abs dots"><i></i><i class="on"></i><i></i><i></i></div>

<div class="abs divider" style="top:470px"><i></i></div>
<h1 class="abs intro">Brantley Fuel provides the full-scale service of a petroleum distributor,<br>delivering gasoline, diesel and lube oils to retail.</h1>
<div class="abs divider" style="top:558px"><i></i></div>

<div class="abs service" style="left:171px">
  <div class="photo" role="img" aria-label="Photo of a white semi truck" style="background-color:#9a9c9e;background-image:linear-gradient(#c5c8cb,#6e6f70)"></div>
  <div class="label">Fuel Delivery</div>
  <p>Brantley Fuel provides fuel delivery for independent gas stations, convenience stores ...</p>
  <a>Read More</a>
</div>
<div class="abs service" style="left:336px">
  <div class="photo" role="img" aria-label="Photo of colourful motor oil jugs on a store shelf" style="background-image:linear-gradient(135deg,#6b4a3a,#c9a23a 50%,#3a3488)"></div>
  <div class="label">Oil</div>
  <p>Looking for speciality auto, tractor, tractor trailer, aviation or other commercial oils ...</p>
  <a>Read More</a>
</div>
<div class="abs service" style="left:501px">
  <div class="photo" role="img" aria-label="Photo of a silver fuel tank trailer in a field" style="background-image:linear-gradient(#b9bcbf,#8e9194 55%,#6f6e68)"></div>
  <div class="label">Farm Fuel</div>
  <p>Looking for gasoline, diesel red diesel off road fuel or farm diesel? We can deliver ...</p>
  <a class="hover">Read More</a>
</div>
<div class="abs service" style="left:666px">
  <div class="photo" role="img" aria-label="Photo of a grey steel cargo container" style="background-image:linear-gradient(#b5b8bb,#7c8186 60%,#6f7a68)"></div>
  <div class="label">Cargo Containers</div>
  <p>Want to purchase or lease a storage container, we have what you need! We can deliver ...</p>
  <a>Read More</a>
</div>

<div class="abs footer-band"></div>
<div class="abs cta"></div>
<div class="abs cta-text">Brantley Fuel makes <span>customer service</span> and <span>satisfaction priority one!</span></div>
<div class="abs cta-btn">Contact Us</div>

<h2 class="abs col-title" style="left:171px">Contact Us</h2>
<div class="abs foot" style="left:171px;top:1020px">
  <div class="hi">Call Us: (555) 214-7730</div>
  <div>info@brantley-fuel.com</div>
  <div class="hi" style="margin-top:9px">Address</div>
  <div>418 Cedar Mill Road, Harlow,<br>TX 75990</div>
</div>

<h2 class="abs col-title" style="left:390px">Quick Links</h2>
<div class="abs foot" style="left:390px;top:1021px">
  <div>About</div><div style="color:var(--red)">Services</div><div>Blog</div><div>Review</div><div>Contact</div>
</div>

<h2 class="abs col-title" style="left:527px">Services</h2>
<div class="abs foot" style="left:527px;top:1021px">
  <div>Fuel Delivery</div><div>Oil</div><div>Farm Fuel</div><div>Cargo Containers</div>
</div>

<h2 class="abs col-title" style="left:666px">Subscribe Us</h2>
<div class="abs subscribe">Enter Your Email...
  <svg width="10" height="9" viewBox="0 0 10 9" aria-hidden="true"><polygon points="0,0 10,4.5 0,9 2,4.5" fill="#e3262e"/></svg>
</div>
<div class="abs social bottom"><i></i><i class="on"></i><i></i><i></i><i></i></div>

<div class="abs rule"></div>
<div class="abs copy">© 2019 <span>Brantley Fuel.</span> All Right Reserved</div>
<svg class="abs" style="left:806px;top:1166px" width="14" height="16" viewBox="0 0 14 16" aria-label="Back to top"><polygon points="7,0 14,16 7,12 0,16" fill="#e3262e"/></svg>

</body>
</html>
```